Celebrate Weekends

Hi Doreen,

I'm looking to do another promo poster for my shop. Please use similar style as GLIMMERAMA poster

Title and description :

CELEBRATE WEEKEND
$10 PHO
ALL DAY SATURDAY & SUNDAY

Order your NOODLE NOOK or Eat-In
Limited Time Only
...............................................................

* Must use these photos in the poster

Shop

```html
<!DOCTYPE html>
<html lang="en">
<head>
<meta charset="utf-8">
<title>Celebrate Weekend – $10 Pho</title>
<link rel="stylesheet" href="https://fonts.googleapis.com/css2?family=Londrina+Solid:wght@400;900&display=swap">
<style>
  :root {
    --page: #2c2c2c;
    --card: #ffffff;
    --board: #2f2f2f;
    --board-light: #3a3a3a;
    --chalk: #ffffff;
    --shadow: #1c1c1c;
    --accent-red: #d42027;
    --logo-ring: #e8892b;
    --photo-dark: #1e1e1e;
    --photo-mid: #6b5a48;
    --photo-light: #f2efe9;
  }
  * { box-sizing: border-box; margin: 0; padding: 0; }
  html, body { width: 849px; height: 1200px; overflow: hidden; background: var(--page); }
  .poster {
    position: relative; width: 849px; height: 1200px; background: var(--page);
    font-family: "Londrina Solid", "Arial Narrow", sans-serif; color: var(--chalk);
  }
  .card {
    position: absolute; left: 42px; top: 40px; width: 764px; height: 1120px;
    background: var(--card);
  }
  .board {
    position: absolute; left: 62px; top: 58px; width: 726px; height: 1086px;
    background: radial-gradient(ellipse at 50% 40%, var(--board-light), var(--board) 75%);
  }
  .frame { position: absolute; left: 0; top: 0; width: 849px; height: 1200px; }
  .headline {
    position: absolute; left: 0; width: 849px; text-align: center; letter-spacing: 1px;
    text-shadow: 3px 3px 0 var(--shadow), 4px 4px 0 var(--chalk);
  }
  .headline--kicker { top: 128px; font-size: 54px; font-weight: 900; line-height: 54px; }
  .headline--price {
    top: 188px; font-size: 150px; font-weight: 900; line-height: 140px; color: var(--accent-red);
    text-shadow: 4px 4px 0 var(--shadow), 6px 6px 0 var(--accent-red);
  }
  .headline--days { top: 342px; font-size: 30px; font-weight: 900; line-height: 32px; text-shadow: 2px 2px 0 var(--shadow); }
  .stamp {
    position: absolute;
    background:
      radial-gradient(circle, var(--board) 5px, transparent 5.5px) 0 -7px / 14px 14px repeat-x,
      radial-gradient(circle, var(--board) 5px, transparent 5.5px) 0 calc(100% + 7px) / 14px 14px repeat-x,
      radial-gradient(circle, var(--board) 5px, transparent 5.5px) -7px 0 / 14px 14px repeat-y,
      radial-gradient(circle, var(--board) 5px, transparent 5.5px) calc(100% + 7px) 0 / 14px 14px repeat-y,
      var(--card);
  }
  .stamp--feature { left: 172px; top: 402px; width: 504px; height: 284px; }
  .stamp--left { left: 172px; top: 700px; width: 241px; height: 287px; }
  .stamp--right { left: 435px; top: 700px; width: 242px; height: 287px; }
  .photo {
    position: absolute; inset: 18px 16px; border: 3px solid var(--photo-dark);
    background: radial-gradient(ellipse at 50% 55%, var(--photo-light) 0 30%, var(--photo-mid) 42%, var(--photo-dark) 80%);
  }
  .cta {
    position: absolute; left: 0; width: 849px; text-align: center; font-weight: 900;
    font-size: 31px; line-height: 33px; letter-spacing: 1px; text-shadow: 2px 2px 0 var(--shadow);
  }
  .cta--order { top: 994px; }
  .cta--limited { top: 1027px; }
  .brand {
    position: absolute; left: 373px; top: 1065px; width: 102px; height: 102px;
    background: #000; border: 2px solid var(--chalk);
    display: flex; align-items: center; justify-content: center; text-align: center;
    font-weight: 900; font-size: 22px; line-height: 22px; color: var(--logo-ring);
  }
</style>
</head>
<body>
<main class="poster">
  <div class="card"></div>
  <div class="board"></div>
  <svg class="frame" viewBox="0 0 849 1200" aria-hidden="true">
    <path d="M92 66 H758 A22 22 0 0 0 780 88 V1113 A22 22 0 0 0 758 1135 H92 A22 22 0 0 0 70 1113 V88 A22 22 0 0 0 92 66 Z" fill="none" stroke="#fff" stroke-width="5"/>
    <path d="M98 78 H752 A16 16 0 0 0 768 94 V1107 A16 16 0 0 0 752 1123 H98 A16 16 0 0 0 82 1107 V94 A16 16 0 0 0 98 78 Z" fill="none" stroke="#fff" stroke-width="2"/>
  </svg>

  <h1 class="headline headline--kicker">CELEBRATE WEEKEND</h1>
  <h2 class="headline headline--price">$10 PHO</h2>
  <p class="headline headline--days">ALL DAY SATURDAY &amp; SUNDAY</p>

  <div class="stamp stamp--feature"><div class="photo" role="img" aria-label="Bowl of chicken pho with herbs, red onion, bean sprouts and lime"></div></div>
  <div class="stamp stamp--left"><div class="photo" role="img" aria-label="Bowl of tofu pho with spring onion and herbs"></div></div>
  <div class="stamp stamp--right"><div class="photo" role="img" aria-label="Bowl of beef ball pho with red onion and herbs"></div></div>

  <p class="cta cta--order">ORDER YOUR PHO TO GO OR EAT-IN</p>
  <p class="cta cta--limited">LIMITED TIME ONLY</p>

  <div class="brand">NOODLE<br>NOOK</div>
</main>
</body>
</html>
```